Delvane Advisory Partners
Simple
Dr. Paul Merideth
347 Brookfield Lane
Los Altos, CA 94024
mtorvell@delvaneadvisorypartners.example
www.delvaneadvisorypartners.example
I wish to create a classy, simple, elegant single-sided business card for my consulting company.
I only wish for my number, e-mail, and website information to be on the card, NOT my address. Also, no need to put "cell" or "e-mail" or "web" on the card, just the information.

```html
<!DOCTYPE html>
<html lang="en">
<head>
<meta charset="utf-8">
<title>Delvane Advisory Partners — Business Card</title>
<link rel="stylesheet" href="https://fonts.googleapis.com/css2?family=Source+Sans+3:wght@400;700&family=Tinos&display=swap">
<style>
  :root {
    --backdrop: #e9e6e1;
    --card: #ffffff;
    --ink: #1a1a1a;
    --ink-soft: #555555;
    --band-dark: #141414;
    --band-grey: #8a8a8a;
    --band-grey-light: #b9b9b9;
  }
  * { margin: 0; padding: 0; box-sizing: border-box; }
  html, body {
    width: 1200px;
    height: 780px;
    overflow: hidden;
    background: var(--backdrop);
  }
  .canvas {
    position: relative;
    width: 1200px;
    height: 780px;
    display: flex;
    align-items: center;
    justify-content: center;
  }
  .business-card {
    position: relative;
    width: 1000px;
    height: 580px;
    background: var(--card);
    border-radius: 34px;
    overflow: hidden;
    box-shadow: 0 10px 30px rgba(0,0,0,0.18);
    text-align: center;
    color: var(--ink);
  }
  .company-name {
    position: absolute;
    top: 96px;
    left: 0;
    right: 0;
    font-family: "Tinos", "Times New Roman", serif;
    font-size: 52px;
    letter-spacing: 4px;
    color: var(--ink);
    text-transform: uppercase;
  }
  .holder {
    position: absolute;
    top: 232px;
    left: 0;
    right: 0;
    font-family: "Source Sans 3", Arial, sans-serif;
  }
  .holder-name {
    font-size: 30px;
    font-weight: 700;
    color: var(--ink);
    line-height: 1.1;
  }
  .holder-company {
    font-size: 24px;
    color: var(--ink-soft);
    line-height: 1.2;
  }
  .contact {
    position: absolute;
    top: 346px;
    left: 0;
    right: 0;
    font-family: "Tinos", "Times New Roman", serif;
    font-size: 23px;
    line-height: 34px;
    color: var(--ink);
    list-style: none;
  }
  .contact .phone { margin-bottom: 10px; }
  .edge-band {
    position: absolute;
    left: 0;
    bottom: 0;
    width: 1000px;
    height: 80px;
  }
</style>
</head>
<body>
  <main class="canvas">
    <article class="business-card">
      <h1 class="company-name">Delvane Advisory Partners</h1>
      <div class="holder">
        <p class="holder-name">Dr. Paul Merideth</p>
        <p class="holder-company">Delvane Advisory Partners</p>
      </div>
      <ul class="contact">
        <li class="phone">650-555-0143</li>
        <li class="email">mtorvell@delvaneadvisorypartners.example</li>
        <li class="web">www.delvaneadvisorypartners.example</li>
      </ul>
      <svg class="edge-band" viewBox="0 0 1000 80" preserveAspectRatio="none" aria-hidden="true">
        <defs>
          <linearGradient id="greyBand" x1="0" y1="0" x2="1" y2="0">
            <stop offset="0" stop-color="var(--band-grey)"/>
            <stop offset="1" stop-color="var(--band-grey-light)"/>
          </linearGradient>
        </defs>
        <path d="M0 58 L720 44 L1000 10 L1000 80 L0 80 Z" fill="url(#greyBand)"/>
        <path d="M0 58 L640 50 Q700 48 740 64 L770 80 L0 80 Z" fill="var(--band-dark)"/>
      </svg>
    </article>
  </main>
</body>
</html>
```